Halvard Catamaran

We need a website to explain how a competent person can build our sixty foot ocean cruising catamaran.

We will supply the drawings as computer files that can be used in any 3D cutting machine.

All the shapes to make the boat are cut perfectly by machine saving thousands of hours.

We are university qualified engineers mathematicians and designers and we have developed these designs over many years. We are now willing to share our intellectual property.

Target Market(s)

Potential boat builders who want to criuse the world oceans

Coding

Coded - Design and coding required

Number of Pages Required

4 page

Font styles to use
Sans Serif

Colors
85acd3
ffffff
ffc214
cee9f5
fbf289

Requirements
Must have
• The website should
- make us look professional - engineers, mathematicians, marine designers
- make it seem possible that someone with reasonable skills can undertake this project
- persuade the visitor to the site to buy study plans as a first step
Nice to have
• Uncluttered, not flashy, elegant, lots of space, lots of white
Should not have
• No pictures of other boats
No quick images flashing around the screen

```html
<!DOCTYPE html>
<html lang="en">
<head>
<meta charset="utf-8">
<title>Halvard Catamaran</title>
<link href="https://fonts.googleapis.com/css2?family=Montserrat:wght@400;500;600&family=Nunito+Sans:wght@300;400;600&display=swap" rel="stylesheet">
<style>
:root{
  --blue:#85acd3;
  --blue-ink:#2c5680;
  --navy:#1d3957;
  --yellow:#ffc214;
  --pale:#cee9f5;
  --cream:#fbf289;
  --white:#ffffff;
  --ink:#1f2b38;
}
*{box-sizing:border-box;margin:0;padding:0}
html,body{width:1200px;height:4743px;overflow:hidden;background:var(--white)}
body{position:relative;font-family:"Nunito Sans",Arial,sans-serif;color:var(--ink)}
.abs{position:absolute}
.head{font-family:Montserrat,Arial,sans-serif;font-weight:500}
.img{position:absolute}

/* hero */
.hero{left:0;top:0;width:1200px;height:688px;background:linear-gradient(100deg,#5f8fbf 0%,var(--blue) 45%,var(--blue-ink) 100%)}
.site-title{width:1200px;text-align:center;color:var(--white);font-size:26px}
.nav{left:178px;top:112px;width:842px;height:44px;background:var(--navy);display:flex;align-items:center;font-family:Montserrat,Arial,sans-serif;font-size:12px;color:var(--white)}
.nav a{color:var(--white);text-decoration:none;height:100%;display:flex;align-items:center;padding:0 27px}
.nav a.active{background:var(--yellow);color:var(--navy);font-weight:600;padding:0 34px}
.nav .sep{opacity:.7}
.hero h1{top:290px;width:1200px;text-align:center;color:var(--white);font-size:46px;line-height:60px}
.hero .inquiry{top:438px;width:1200px;text-align:center;font-family:Montserrat,Arial,sans-serif;font-size:15px}
.hero .inquiry a{color:var(--cream)}
.dots{top:612px;left:528px;display:flex;gap:20px}
.dots span{width:13px;height:13px;background:var(--white)}
.dots span.on{background:var(--yellow)}

/* intro */
.quote{top:750px;width:1200px;text-align:center;font-size:33px;line-height:42px;font-weight:300;color:var(--ink)}
.quote .by{font-size:37px;line-height:48px;font-weight:400}
.intro{top:906px;left:250px;width:700px;text-align:center;font-size:12px;line-height:23px;color:#333}
.btn{display:flex;align-items:center;justify-content:center;border-radius:20px;background:var(--yellow);color:var(--navy);font-family:Montserrat,Arial,sans-serif;font-weight:500;font-size:14px;text-decoration:none}

/* gallery */
.tech{left:0;top:1078px;width:432px;height:475px;background:linear-gradient(135deg,var(--blue),var(--blue-ink))}
.tech .frame{position:absolute;left:22px;top:24px;width:388px;height:426px;border:3px solid var(--white);display:flex;align-items:center;justify-content:center;color:var(--white);font-family:Montserrat,Arial,sans-serif;font-size:22px}

/* feature sections */
.h2{color:var(--blue-ink);font-size:37px;line-height:55px}
.box{border:4px solid var(--blue);background:var(--white)}
.box p,.box li{color:var(--blue-ink);font-size:12px;line-height:22.5px}
.box p+p{margin-top:22px}
.box ul{list-style:circle;padding-left:18px;margin-top:12px}
.box li{font-size:11px}
.lead{font-family:Montserrat,Arial,sans-serif;font-size:13.5px !important;line-height:23px !important}

/* band */
.band{left:0;top:3557px;width:1200px;height:531px;background:linear-gradient(100deg,var(--pale) 0%,var(--blue) 100%)}
.card{position:absolute;border:3px solid var(--white);background:rgba(255,255,255,.18);color:var(--navy);padding:26px 22px}
.card h3{font-family:Montserrat,Arial,sans-serif;font-weight:500;font-size:19px;line-height:26px;margin-bottom:20px}
.card p{font-size:11.5px;line-height:22.5px}

/* cta */
.cta{top:4162px;left:220px;width:760px;text-align:center;color:var(--blue-ink);font-size:26px;line-height:36.5px}
.cta-mail{top:4303px;width:1200px;text-align:center;color:var(--blue-ink);font-size:34px}
.cta-mail a{color:var(--blue-ink)}

/* footer */
.footer{left:0;top:4457px;width:1200px;height:286px;background:var(--navy);color:var(--white)}
.footer .lines{position:absolute;top:96px;width:1200px;text-align:center;font-family:Montserrat,Arial,sans-serif;font-size:12px;line-height:23px}
.social{position:absolute;top:168px;left:496px;display:flex;gap:38px}
.social span{width:22px;height:22px;border-radius:50%;background:var(--cream)}
.copy{position:absolute;top:210px;width:1200px;text-align:center;font-family:Montserrat,Arial,sans-serif;font-size:12px}
</style>
</head>
<body>

<section class="abs hero" role="img" aria-label="Hero photo of a catamaran hull under construction in a workshop, tinted blue">
  <div class="abs site-title head" style="top:44px">The Halvard Catamaran</div>
  <nav class="abs nav">
    <a class="active" href="#">Halvard 60</a><span class="sep">|</span>
    <a href="#">Hulls</a><span class="sep">|</span>
    <a href="#">Wing Mast</a><span class="sep">|</span>
    <a href="#">Construction Technique</a><span class="sep">|</span>
    <a href="#">Bridge Deck</a><span class="sep">|</span>
    <a href="#">Specifications</a>
  </nav>
  <h1 class="abs head">Build A 60-Foot Ocean<br>Cruising Catamaran</h1>
  <div class="abs inquiry"><a href="#">Sale Inquiry: sales@thehalvardcatamaran.com</a></div>
  <div class="abs dots"><span></span><span></span><span></span><span class="on"></span><span></span></div>
</section>

<div class="abs quote">Those who fall in love with practice without science are like<br>a sailor who steers a ship without a helm or compass …<br><span class="by">~ Aurelio Benedetti</span></div>
<p class="abs intro">The Halvard Catamaran is a stunning 18+ metre (62 feet) ocean sail boat that you can build yourself for under $200,000. This beautiful twin hulled catamaran is light, strong and stable with superb upwind performance, advanced aerodynamics with minimal fairing, and an easy build methodology.</p>
<a class="abs btn" href="#" style="left:541px;top:1008px;width:117px;height:37px">Hulls</a>

<div class="abs tech" role="img" aria-label="Workshop photo tinted blue"><div class="frame">Technical Constructions</div></div>
<div class="img" style="left:449px;top:1080px;width:304px;height:247px;background:linear-gradient(90deg,#9ea3a8,#d8dadc 50%,#2a2a2a)" role="img" aria-label="3D render of the deck viewed from above"></div>
<div class="img" style="left:767px;top:1080px;width:433px;height:203px;background:linear-gradient(120deg,#d9d0c4,#a0704a 50%,#6b4a30)" role="img" aria-label="Photo of timber hull frames on the building jig"></div>
<div class="img" style="left:449px;top:1351px;width:304px;height:202px;background:linear-gradient(160deg,#e6e6e6,#9a9a9a 60%,#4a4a4a)" role="img" aria-label="3D render of the catamaran with wing mast"></div>
<div class="img" style="left:767px;top:1306px;width:433px;height:247px;background:linear-gradient(160deg,#8fb0c8,#3e6e99 50%,#174a7a)" role="img" aria-label="3D render of the hulls and rudders from below"></div>

<h2 class="abs h2 head" style="left:184px;top:1646px;width:470px">Making Use Of Everything Technology Has To Offer</h2>
<div class="img" style="left:184px;top:1827px;width:512px;height:377px;background:linear-gradient(90deg,#5d7a3a,#8aa06a 45%,#c8c8c8 60%,#9a9a9a)" role="img" aria-label="Photo of a finished hull section outdoors beside a tree"></div>
<div class="abs box" style="left:662px;top:1636px;width:356px;height:484px;padding:42px 34px 0 48px">
  <p>In the last decade there has been a fortunate coincidence of marine design software, 3D CAD software and computer controlled milling machines. Australian made ply from sustainable forests, cut by CNC, has been used throughout to build frames and bulkheads accurate to a fraction of a millimetre.</p>
  <p>The ply hull shells have been overlaid with Tidewell epoxy with uniaxial and bi-axial glass. The inner surfaces have been lined with foam and epoxy laminate – all vacuum bagged for maximum strength.</p>
  <p>High stress areas have been reinforced with carbon fibre. The boat is strong and light – ten tonnes is the unloaded target weight.</p>
</div>

<div class="abs box" style="left:184px;top:2260px;width:353px;height:483px;padding:40px 34px 0 34px">
  <p class="lead">The Halvard Catamaran is designed to be exhilarating while using the latest techniques and innovation to maximise safety:</p>
  <ul>
    <li>The sharp, low buoyancy X bows pierce through wind chop to minimise pitching</li>
    <li>Hull wetted surface drag has been reduced to the bare minimum using successive iterations of hydrostatic software</li>
    <li>The rotating mast's D shape comes from research by R T Calloway and Owen Strand and is expected to achieve a 100% improvement in lift to drag ratio over round masts</li>
  </ul>
  <a class="btn" href="#" style="width:117px;height:37px;margin-top:22px">Read More</a>
</div>
<h2 class="abs h2 head" style="left:563px;top:2268px;width:460px">Designed With Safety And Excitement In Mind</h2>
<div class="img" style="left:506px;top:2451px;width:512px;height:377px;background:linear-gradient(90deg,#e4e4e4,#b8bcc0 50%,#1a1a1a)" role="img" aria-label="3D render of the bridge deck and bows from above"></div>

<h2 class="abs h2 head" style="left:197px;top:2903px;width:420px">Halvard 60<br>Features</h2>
<div class="img" style="left:184px;top:3049px;width:512px;height:414px;background:linear-gradient(180deg,#54586c,#8a8e9a 50%,#5e6070)" role="img" aria-label="3D side render of the catamaran cabin and hull"></div>
<div class="abs box" style="left:662px;top:2894px;width:356px;height:486px;padding:42px 34px 0 46px">
  <p class="lead">The Halvard 60 is easily handled by one person either from the cockpit or from the safety and comfort of an internal chart room with forwarding visibility.</p>
  <p class="lead">Have a look at these other superb features:</p>
  <ul>
    <li>Dedicated electric winch for mainsail halyard inside the main beam</li>
    <li>Self-tacking headsail and rotating carbon fibre wing mast</li>
    <li>Electric winches that can be controlled remotely for main sheet at the helm</li>
    <li>Sheltered cockpit helm stations</li>
  </ul>
  <a class="btn" href="#" style="width:120px;height:37px;margin-top:18px">Read More</a>
</div>

<section class="abs band" role="img" aria-label="Cloudy sky photo tinted pale blue">
  <div class="card" style="left:182px;top:105px;width:212px;height:316px"><h3>Stunning 18+ Metre Sail Boat</h3><p>At 62 feet or 18.9 metres, this stunning ocean going sail boat is not only huge, it's designed for maximum performance while being lightweight, fast and safe in all weather conditions.</p></div>
  <div class="card" style="left:392px;top:77px;width:212px;height:364px"><h3>Every Component Optimised</h3><p>To maximise performance, everything from the plumb X bows to the kick up transom hung rudders has been optimised with the objective that this boat will sail to windward in a six knot breeze and remain safe in 60 knots.</p></div>
  <div class="card" style="left:602px;top:105px;width:211px;height:316px"><h3>Every Detail Researched And Analysed</h3><p>The boat is designed to sail efficiently in light conditions therefore every little detail of its construction has been research and analysed to ensure it will fly upwind.</p></div>
  <div class="card" style="left:811px;top:105px;width:209px;height:316px;padding-top:18px"><h3>Two Queen-Sized Cabins</h3><p>In each of the two hulls there is a spacious and well-appointed queen-sized cabin, a 2.5 metre bathroom behind, and bunks and heads in the fore cabins for crew or other passengers.</p></div>
</section>

<p class="abs cta head">For more information on how you can build this beautiful ocean cruising sail boat for under $200,000, email The Halvard Catamaran</p>
<p class="abs cta-mail head">on <a href="#">sales@thehalvardcatamaran.com</a></p>
<a class="abs btn" href="#" style="left:541px;top:4376px;width:117px;height:36px">Contact</a>

<footer class="abs footer" role="contentinfo">
  <div class="abs site-title head" style="top:42px;font-size:24px">The Halvard Catamaran</div>
  <div class="lines">p.lindqvist@mailbox.example &nbsp;&nbsp;|&nbsp;&nbsp; sales@thehalvardcatamaran.com<br>engineering@thehalvardcatamaran.com &nbsp;&nbsp;|&nbsp;&nbsp; accounts@thehalvardcatamaran.com</div>
  <div class="social" aria-label="Social links"><span></span><span></span><span></span><span></span></div>
  <div class="copy">© 2020 &nbsp;|&nbsp; www.companyname.com</div>
</footer>

</body>
</html>
```